Package Design for 15 lines of Tea

I need design variations for 15 different Tea lines.
The tea will be packaged in Tin cylinders.
I have attached several pictures to show you an example of the display we are modelling after along with other references.
The 15 tea lines are:
Study Tea
Ingredients: Brazilian Mate, Mint
Energy Boost Tea
Ingredients: Yunnan Coffee, Dark Puer
Relaxation Tea
Ingredients: Lotus Flower, South African Rooibos
Beauty Tea
Ingredients: Rose, Chrysanthemum, Red Dates, Huangqi
Sore Throat Tea
Ingredients: Honeysuckle, Pang Da Hai, Chamomile, Licorice Root
Get Well Tea
Ingredients: Ginger, Rooibos, Orange peel, Chinese Angelica
Diet Tea
Ingredients: Puer, Hibiscus, Lemongrass, Lotus Plumule
Bedtime Tea
Ingredients: Apple, Orange, Chamomile
South African Rooibos Tea
(pure)
Brazilian Yerba Mate Tea
(pure)
Long Jing Green Tea
(pure)
Darjeeling Black Tea
(pure)
Nepal Golden Tea
(Pure)
Bai Mu Dan White Tea
(pure)
Phoenix Oolong Tea
(pure)
Every Tea Blend should have three unique symbols that describe the purpose and theme of the blend. (!!Please don't make specific reference to the ingredients of the blends because some of these ingredients may be changed later. Stick to focusing on the intended purpose of the tea blend!!)
I would like the symbols to keep the same brushlike style that is consistent with our company logo.
Please keep the three block structure. I suggest keeping to just one color per tea blend. This will help each blend stand out between one another. I have a sample of the "Diet Tea" attached that I did myself to give you an idea of the structure I'm looking for, but obviously it's just my amateur version. Hope you can make them look far more appealing.
The ultimate goal is to build a picture language unique to our brand. As more products are released, we intend to potentially have hundreds of symbols, each with it's own meaning. So it would be nice when you present your pictures if you explain its intended meaning or message.
Deminsions:
Cylinder type 1: 82mm*38mmH
circular labels (along with your design) will be placed on the cap of product, and then the cylinder will be slanted on it's side to display the cap towards the customer.
Cylinder type 2: 65mm*152mmH
the labels will be placed on the side of the cylinder. In this version, try lining the three symbols in a vertical position. If this looks awful to you then feel free to go back to the horizontal style, but it would be nice to see what the vertical version looks like for reference.
Updates
Due to the scope of this project, please take note that I just increased my budget an additional 500 dollars more.
I also just added a 100 dollar second place prize. Don't want to see hard work unrewarded.
Feel free to send a few samples and I will provide prompt feedback. Please don't feel that you must submit all 15 lines at the same time.
Project Deadline Extended
Reason: I am extending the deadline as I feel there are more detailed revisions that need to be made until final selection.
Target Market(s)
Middle to Upper Class Consumers in China
Industry/Entity Type
It Company
Other font styles liked:
- font similar to font on company logo
Requirements
Must have
- Tea Designs must be in harmony with company logo and theme.
Should not have
- Avoid using Chinese characters as symbols. They may seem cool to westerners, but it's tacky for Chinese consumers.

```html
<!DOCTYPE html>
<html lang="en">
<head>
<meta charset="utf-8">
<title>Lumo Tea – Cap Label Variations</title>
<link rel="stylesheet" href="https://fonts.googleapis.com/css2?family=Bree+Serif&family=Cabin:wght@400;500&display=swap">
<style>
  :root {
    --bg-center: #ffffff;
    --bg-edge: #a8a8ad;
    --caption: #4a4a4f;
    --divider: #8e8e92;
    --ink: #ffffff;
    --study-light: #7cbbe6;
    --study-dark: #1d5795;
    --study-band: #0c4e8b;
    --energy-light: #e7a617;
    --energy-dark: #8b4a2c;
    --beauty-light: #9a70b2;
    --beauty-dark: #3c1858;
  }
  html, body { margin: 0; padding: 0; overflow: hidden; }
  .sheet {
    position: relative;
    width: 1200px;
    height: 927px;
    overflow: hidden;
    background: radial-gradient(ellipse 60% 62% at 50% 48%, var(--bg-center) 30%, var(--bg-edge) 100%);
    font-family: "Cabin", Arial, sans-serif;
  }
  .caption {
    position: absolute;
    left: 118px;
    margin: 0;
    font: 400 15px/16px Arial, Helvetica, sans-serif;
    color: var(--caption);
  }
  .caption--top { top: 93px; }
  .caption--bottom { top: 527px; }
  .divider { position: absolute; left: 170px; top: 452px; width: 860px; height: 24px; }

  .cap {
    position: absolute;
    width: 236px;
    height: 236px;
    border-radius: 50%;
    color: var(--ink);
    text-align: center;
    overflow: hidden;
    box-shadow: inset 0 0 0 3px rgba(0,0,0,.12);
  }
  .cap--study  { background: linear-gradient(225deg, var(--study-light) 0%, var(--study-dark) 100%); }
  .cap--energy { background: linear-gradient(225deg, var(--energy-light) 10%, var(--energy-dark) 100%); }
  .cap--beauty { background: linear-gradient(225deg, var(--beauty-light) 0%, var(--beauty-dark) 100%); }
  .cap--split  { background: linear-gradient(180deg, #5d9bd2 0%, #79b3e2 50%, var(--study-band) 50%, var(--study-band) 100%); }

  .cap__ring { position: absolute; inset: 0; }
  .cap__title {
    position: absolute; left: 0; right: 0; margin: 0;
    font: 400 27px/30px "Bree Serif", Georgia, serif;
    letter-spacing: .2px;
  }
  .cap__meta {
    position: absolute; left: 0; right: 0;
    display: flex; justify-content: center; align-items: center; gap: 7px;
  }
  .cap__icon { width: 14px; height: 14px; }
  .cap__ingredients {
    margin: 0 0 0 4px;
    font-size: 7px; line-height: 8px; text-align: left;
  }
  .brand {
    position: absolute; left: 0; right: 0;
    display: flex; justify-content: center; align-items: center; gap: 5px;
    font: 400 13px/14px "Bree Serif", Georgia, serif;
  }
  .brand__mark { width: 9px; height: 9px; background: var(--ink); }

  /* placements */
  .pos-a { left: 188px; top: 157px; }
  .pos-b { left: 482px; top: 157px; }
  .pos-c { left: 775px; top: 157px; }
  .pos-d { left: 481px; top: 534px; }
  .pos-e { left: 775px; top: 534px; }

  .layout-main .cap__title { top: 61px; }
  .layout-main .cap__meta { top: 92px; }
  .layout-main .brand { top: 136px; }

  .layout-split .cap__title {
    left: 52px; right: auto; top: 66px;
    font-size: 19px; line-height: 22px; text-align: left; white-space: nowrap;
  }
  .layout-split .book { position: absolute; left: 142px; top: 64px; width: 40px; height: 32px; }
  .layout-split .cap__sub {
    position: absolute; left: 52px; top: 89px; margin: 0;
    font-size: 9px; line-height: 10px; text-align: left; white-space: nowrap;
  }
  .layout-split .brand { top: 142px; }

  .layout-stack .brand { top: 55px; }
  .layout-stack .cap__title { top: 122px; font-size: 26px; }
  .layout-stack .cap__sub { position: absolute; left: 0; right: 0; top: 153px; margin: 0; font-size: 8px; }
  .layout-stack .cap__meta { top: 167px; }
</style>
</head>
<body>
<main class="sheet">
  <p class="caption caption--top">Favorite design<br>with 3 flavor variation</p>

  <svg width="0" height="0" style="position:absolute" aria-hidden="true">
    <defs>
      <symbol id="ring" viewBox="0 0 236 236">
        <circle cx="118" cy="118" r="104" fill="none" stroke="#fff" stroke-width="2.6" opacity=".95"/>
        <circle cx="118.6" cy="117.4" r="101.5" fill="none" stroke="#fff" stroke-width="1" opacity=".6" stroke-dasharray="40 6 22 4 60 8"/>
        <circle cx="117.4" cy="118.8" r="106.2" fill="none" stroke="#fff" stroke-width=".9" opacity=".55" stroke-dasharray="30 10 50 5 18 7"/>
      </symbol>
      <symbol id="i-pencil" viewBox="0 0 14 14"><path d="M2 12l1-3 7-7 2 2-7 7z" fill="#fff"/></symbol>
      <symbol id="i-book" viewBox="0 0 14 14"><path d="M1 3h5l1 1 1-1h5v8H8l-1 1-1-1H1zM7 4v8" fill="none" stroke="#fff" stroke-width="1.2"/></symbol>
      <symbol id="i-laptop" viewBox="0 0 14 14"><path d="M3 3h8v6H3zM1 11h12" fill="none" stroke="#fff" stroke-width="1.3"/></symbol>
      <symbol id="i-bolt" viewBox="0 0 14 14"><path d="M8 1L3 8h4l-1 5 5-7H7z" fill="#fff"/></symbol>
      <symbol id="i-refresh" viewBox="0 0 14 14"><path d="M11.5 7A4.5 4.5 0 1 1 9.5 3.2" fill="none" stroke="#fff" stroke-width="1.6"/><path d="M8 1h4v4z" fill="#fff"/></symbol>
      <symbol id="i-chart" viewBox="0 0 14 14"><rect x="1.5" y="2" width="11" height="10" fill="none" stroke="#fff" stroke-width="1.2"/><path d="M3 10l3-3 2 2 3-4v5z" fill="#fff"/></symbol>
      <symbol id="i-flower" viewBox="0 0 14 14"><g fill="#fff"><circle cx="7" cy="3" r="1.6"/><circle cx="7" cy="11" r="1.6"/><circle cx="3" cy="7" r="1.6"/><circle cx="11" cy="7" r="1.6"/><circle cx="7" cy="7" r="1"/></g></symbol>
      <symbol id="i-heart" viewBox="0 0 14 14"><path d="M7 12S1.5 8.5 1.5 5A2.7 2.7 0 0 1 7 4a2.7 2.7 0 0 1 5.5 1C12.5 8.5 7 12 7 12z" fill="none" stroke="#fff" stroke-width="1.3"/></symbol>
      <symbol id="i-sparkle" viewBox="0 0 14 14"><path d="M8 2l1 4 4 1-4 1-1 4-1-4-4-1 4-1zM3 1l.5 1.5L5 3l-1.5.5L3 5l-.5-1.5L1 3l1.5-.5z" fill="#fff"/></symbol>
    </defs>
  </svg>

  <section class="cap cap--study layout-main pos-a">
    <svg class="cap__ring" viewBox="0 0 236 236" aria-hidden="true"><use href="#ring"/></svg>
    <h2 class="cap__title">Study Tea</h2>
    <div class="cap__meta">
      <svg class="cap__icon"><use href="#i-pencil"/></svg>
      <svg class="cap__icon"><use href="#i-book"/></svg>
      <svg class="cap__icon"><use href="#i-laptop"/></svg>
      <p class="cap__ingredients">Brazilian Mate<br>&amp; Mint</p>
    </div>
    <div class="brand"><span class="brand__mark"></span>Lumo Tea</div>
  </section>

  <section class="cap cap--energy layout-main pos-b">
    <svg class="cap__ring" viewBox="0 0 236 236" aria-hidden="true"><use href="#ring"/></svg>
    <h2 class="cap__title">Energy Tea</h2>
    <div class="cap__meta">
      <svg class="cap__icon"><use href="#i-bolt"/></svg>
      <svg class="cap__icon"><use href="#i-refresh"/></svg>
      <svg class="cap__icon"><use href="#i-chart"/></svg>
      <p class="cap__ingredients">Yunnan Coffee<br>&amp; Dark Puer</p>
    </div>
    <div class="brand"><span class="brand__mark"></span>Lumo Tea</div>
  </section>

  <section class="cap cap--beauty layout-main pos-c">
    <svg class="cap__ring" viewBox="0 0 236 236" aria-hidden="true"><use href="#ring"/></svg>
    <h2 class="cap__title">Beauty Tea</h2>
    <div class="cap__meta">
      <svg class="cap__icon"><use href="#i-flower"/></svg>
      <svg class="cap__icon"><use href="#i-heart"/></svg>
      <svg class="cap__icon"><use href="#i-sparkle"/></svg>
      <p class="cap__ingredients">Rose, Chrysanthemum,<br>Red Dates &amp; Huangqi</p>
    </div>
    <div class="brand"><span class="brand__mark"></span>Lumo Tea</div>
  </section>

  <svg class="divider" viewBox="0 0 860 24" aria-hidden="true">
    <path d="M2 12 C120 7 300 6 520 8 S800 9 858 10 L800 13 C600 14 420 16 240 20 L230 17 C150 16 60 15 2 12Z" fill="var(--divider)" opacity=".85"/>
    <path d="M40 10 L760 9" stroke="#fff" stroke-width=".6" opacity=".5"/>
  </svg>

  <p class="caption caption--bottom">2 label variation</p>

  <section class="cap cap--split layout-split pos-d">
    <svg class="cap__ring" viewBox="0 0 236 236" aria-hidden="true"><use href="#ring"/></svg>
    <h2 class="cap__title">Study Tea</h2>
    <svg class="book" viewBox="1 3 12 9" preserveAspectRatio="none" aria-hidden="true"><use href="#i-book"/></svg>
    <p class="cap__sub">Brazilian Mate, Mint</p>
    <div class="brand"><span class="brand__mark"></span>Lumo Tea</div>
  </section>

  <section class="cap cap--study layout-stack pos-e">
    <svg class="cap__ring" viewBox="0 0 236 236" aria-hidden="true"><use href="#ring"/></svg>
    <div class="brand"><span class="brand__mark"></span>Lumo Tea</div>
    <h2 class="cap__title">Study Tea</h2>
    <p class="cap__sub">Brazilian Mate &amp; Mint</p>
    <div class="cap__meta">
      <svg class="cap__icon"><use href="#i-pencil"/></svg>
      <svg class="cap__icon"><use href="#i-book"/></svg>
      <svg class="cap__icon"><use href="#i-laptop"/></svg>
    </div>
  </section>
</main>
</body>
</html>
```